BRINDLEWOOD MEDICAL SERVICES , stationary design

Clean , minimal , modern

Target Market(s)

Healthcare

Font styles to use
Sans Serif
Other font styles liked:
• Sans serif rounded light

Colors
b1b1b1

Requirements
Must have
• Must Have:
• - must have letter head, business card, envelope, fax sheet, id badge, folder, thank you card, notebook, invoice sheet, stamp , received stamp
• Nice to Have:
• - nice to have them all custom made (letterhead,envelope, business card, I’d badge etc
• - you need to change the logo colors , icon to dark blue and logo text to dark grey and another option with dark green icon and dark grey logo text .

```html
<!DOCTYPE html>
<html lang="en">
<head>
<meta charset="utf-8">
<title>Brindlewood Medical Services – Business Card</title>
<link href="https://fonts.googleapis.com/css2?family=Roboto:wght@400;500;700&display=swap" rel="stylesheet">
<style>
  :root {
    --navy: #26306b;
    --navy-deep: #1c2455;
    --grey: #b1b1b1;
    --text-grey: #6a6a6a;
    --paper: #ffffff;
    --backdrop: #d2d2d2;
  }
  * { margin: 0; padding: 0; box-sizing: border-box; }
  html, body { width: 1200px; height: 885px; overflow: hidden; }
  body {
    background: radial-gradient(ellipse at 55% 40%, #e4e4e4 0%, var(--backdrop) 60%, #a9a9a9 100%);
    font-family: "Roboto", sans-serif;
    position: relative;
  }
  .card {
    position: absolute;
    width: 520px;
    height: 297px;
    box-shadow: 0 10px 24px rgba(0,0,0,0.25);
  }
  /* Back side */
  .card-back {
    left: 70px; top: 130px;
    background: linear-gradient(135deg, #2b3680 0%, var(--navy-deep) 100%);
    color: var(--paper);
    display: flex;
    flex-direction: column;
    align-items: center;
    justify-content: center;
  }
  .card-back .brand-name {
    font-weight: 700;
    font-size: 34px;
    letter-spacing: 1px;
    display: flex;
    align-items: center;
    gap: 12px;
  }
  .card-back .brand-mark {
    width: 18px; height: 18px; background: var(--paper);
  }
  .card-back .web {
    position: absolute;
    bottom: 34px;
    font-size: 13px;
    letter-spacing: 2px;
  }
  /* Front side */
  .card-front {
    left: 610px; top: 450px;
    background: var(--paper);
  }
  .card-front .divider {
    position: absolute; left: 0; top: 0;
  }
  .logo-block {
    position: absolute;
    left: 34px; top: 110px;
    width: 200px;
    display: flex;
    align-items: center;
    gap: 10px;
  }
  .logo-block .brand-mark {
    width: 14px; height: 14px; background: var(--navy); flex: none;
  }
  .logo-block .brand-name {
    font-weight: 700;
    font-size: 22px;
    line-height: 1.15;
    color: var(--navy);
  }
  .contact-block {
    position: absolute;
    left: 290px; top: 46px;
    width: 215px;
  }
  .person-name {
    font-weight: 700; font-size: 18px; color: var(--navy); letter-spacing: 0.5px;
  }
  .person-title {
    font-size: 12px; color: var(--grey); margin-bottom: 12px;
  }
  .address {
    font-size: 12px; color: var(--text-grey); line-height: 1.45; margin-bottom: 12px;
  }
  .contact-list { list-style: none; }
  .contact-list li {
    font-size: 12px; color: var(--text-grey);
    display: flex; align-items: center; gap: 9px; line-height: 19px;
  }
  .contact-list svg { width: 11px; height: 11px; fill: var(--navy); flex: none; }
</style>
</head>
<body>

  <section class="card card-back">
    <div class="brand-name"><span class="brand-mark"></span>BRINDLEWOOD</div>
    <div class="web">www.brindlewoodmedical.com</div>
  </section>

  <section class="card card-front">
    <svg class="divider" width="520" height="297" aria-hidden="true">
      <line x1="250" y1="50" x2="280" y2="230" stroke="#d0d0d0" stroke-width="1"/>
    </svg>

    <div class="logo-block">
      <span class="brand-mark"></span>
      <div class="brand-name">Brindlewood<br>Medical Services</div>
    </div>

    <div class="contact-block">
      <div class="person-name">MARCUS HALE</div>
      <div class="person-title">CEO/FOUNDER</div>
      <div class="address">214 Larkspur Road<br>Juneau, Alaska 34112</div>
      <ul class="contact-list">
        <li><svg viewBox="0 0 24 24"><path d="M6.6 10.8a15 15 0 0 0 6.6 6.6l2.2-2.2a1 1 0 0 1 1-.25 11.4 11.4 0 0 0 3.6.57 1 1 0 0 1 1 1V20a1 1 0 0 1-1 1A17 17 0 0 1 3 4a1 1 0 0 1 1-1h3.5a1 1 0 0 1 1 1c0 1.25.2 2.45.57 3.57a1 1 0 0 1-.25 1z"/></svg>555 204 7813</li>
        <li><svg viewBox="0 0 24 24"><path d="M7 1h10a2 2 0 0 1 2 2v18a2 2 0 0 1-2 2H7a2 2 0 0 1-2-2V3a2 2 0 0 1 2-2zm0 3v14h10V4zm5 15.5a1 1 0 1 0 0 2 1 1 0 0 0 0-2z"/></svg>555 391 6620</li>
        <li><svg viewBox="0 0 24 24"><path d="M6 2h12v6H6zM3 9h18v9h-3v4H6v-4H3zm5 7v4h8v-4z"/></svg>555 718 2459</li>
        <li><svg viewBox="0 0 24 24"><path d="M2 5h20v14H2zm2 2v.5l8 5 8-5V7z"/></svg>marcus@brindlewood.com</li>
        <li><svg viewBox="0 0 24 24"><circle cx="12" cy="12" r="10"/></svg>www.brindlewood.com</li>
      </ul>
    </div>
  </section>

</body>
</html>
```